Software Product Flyer Design

A established czech software company needs a marketing flyer to promote their software product and its modules.
The overall feel of the flyer must to be serious, but also eye-catching, enticing, clever and bold to attract customers.
Unifying graphic element is the new product logo.
The flyer would be A4, colour both sides and folded once (to give 4 pages of A5).
Title page - product logo with module name and module icon, short presentation of the product and list of its key features.
Inside pages - detailed informations with screenshots or graphical schemas.
Back side - informations about technical requirements and user support, contacts (address, phone, fax, e-mail, web pages - no social networks).
Product logo, module icon and some images attached.
Updates
Hello,
Reason: For organizational reasons we extending the deadline by 10 days.
FYI: We have uploaded the new ZIP file with previous version of our flyer.
Attached PDF file with text for inner pages.
Target Market(s)
Existing or new customers like municipalities, public authorities and nonprofit organizations.
Industry/Entity Type
Marketing
Requirements
Must have
- Winning designer must provide a template for Adobe InDesign based on his graphic design.
Avoid to using exotic fonts - in Czech we use Latin Extended characters (like áéěíýůčřžšťďň).
Nice to have
- Using graphic motif from product logo like as attached splash screen.

```html
<!DOCTYPE html>
<html lang="en">
<head>
<meta charset="utf-8">
<title>Velora – Flyer</title>
<link rel="stylesheet" href="https://fonts.googleapis.com/css2?family=Arimo:wght@400;700&display=swap">
<style>
  :root {
    --ink: #000000;
    --accent: #f15a22;
    --headline: #e3232b;
    --text-dark: #2e2e2e;
    --paper: #ffffff;
    --photo-light: #eef1f3;
    --photo-mid: #cfd6dc;
    --photo-warm: #d9b8a2;
  }
  * { margin: 0; padding: 0; box-sizing: border-box; }
  html, body { width: 1200px; height: 848px; overflow: hidden; background: var(--paper); }
  .spread {
    position: relative;
    width: 1200px;
    height: 848px;
    overflow: hidden;
    font-family: "Arimo", Arial, sans-serif;
  }
  .photo-area {
    position: absolute;
    inset: 0;
    background:
      radial-gradient(ellipse 260px 320px at 640px 300px, var(--photo-warm) 0%, rgba(217,184,162,0) 70%),
      radial-gradient(ellipse 340px 220px at 1040px 640px, #e6e9ec 0%, rgba(230,233,236,0) 75%),
      linear-gradient(135deg, var(--photo-mid) 0%, var(--photo-light) 55%, #f6f7f8 100%);
  }
  .shapes { position: absolute; inset: 0; }
  .fold-line {
    position: absolute;
    left: 599px;
    top: 0;
    width: 1.5px;
    height: 848px;
    background: rgba(255,255,255,0.85);
  }
  .brand {
    position: absolute;
    display: flex;
    align-items: center;
    font-weight: 700;
    letter-spacing: -0.02em;
    line-height: 1;
  }
  .brand-mark {
    display: inline-block;
    background: var(--accent);
    border-radius: 6px;
  }
  .back-brand {
    left: 48px;
    top: 382px;
    font-size: 96px;
    color: var(--paper);
    gap: 16px;
  }
  .back-brand .brand-mark { width: 46px; height: 46px; }
  .contact {
    position: absolute;
    left: 60px;
    width: 400px;
    top: 530px;
    text-align: center;
    color: var(--paper);
    font-size: 15.5px;
    line-height: 21px;
    font-style: normal;
  }
  .front-brand {
    right: 36px;
    top: 100px;
    font-size: 72px;
    color: #3a3a3c;
    gap: 12px;
  }
  .front-brand .brand-mark { width: 34px; height: 34px; border-radius: 5px; }
  .tagline {
    position: absolute;
    right: 36px;
    top: 193px;
    text-align: right;
    font-size: 26px;
    line-height: 34px;
    color: var(--text-dark);
  }
  .tagline strong { color: var(--headline); font-weight: 700; display: block; }
</style>
</head>
<body>
<main class="spread">
  <div class="photo-area" role="img" aria-label="Photograph of a smiling businessman holding a mobile phone and working on a laptop in a bright office"></div>

  <svg class="shapes" width="1200" height="848" viewBox="0 0 1200 848" aria-hidden="true">
    <polygon class="black-field" points="0,0 144,0 600,487 942,848 0,848" fill="var(--ink)"/>
    <polygon class="orange-diamond" points="600,490 852,745 600,1000 346,745" fill="var(--accent)"/>
  </svg>

  <div class="fold-line"></div>

  <section class="back-page">
    <div class="brand back-brand">
      <span class="brand-mark"></span>
      <span class="brand-name">velora</span>
    </div>
    <address class="contact">
      012 Some Street. New York, NY, 12345. USA<br>
      (123) 456-7890<br>
      contact@companyname.com
    </address>
  </section>

  <section class="front-page">
    <div class="brand front-brand">
      <span class="brand-mark"></span>
      <span class="brand-name">velora</span>
    </div>
    <p class="tagline">
      <strong>Lorem ipsum dolor</strong>
      sit amet, consectetur<br>
      adipiscing elit.
    </p>
  </section>
</main>
</body>
</html>
```